Web Design for Cloud Software Solution for Oil Field

Web Design for Company that created software for field data gathering and workflow automation solution built for realization of digital oilfield for all companies for efficient & safe production of energy of the future. Company mission is to connect every field equipment and worker including back office to provide a seamless connected field operation. Reduce operational spending without upfront capital investment. Provide self-learning digital solutions at every step of the way assisting. Goal is to get visitor to schedule a demo.

Target Market(s)

Old Field Operators, Operations managers

Coding

Coded - Design and coding required

Font styles to use
Sans Serif

Colors
0255a3
acd036
1b1b1b
eaeaea

Requirements
Must have
• Slider, testimonial section

```html
<!DOCTYPE html>
<html lang="en">
<head>
<meta charset="utf-8">
<title>Ovrelda — Connected Field Operations</title>
<link rel="stylesheet" href="https://fonts.googleapis.com/css2?family=Arvo:wght@400;700&family=Open+Sans:wght@400;600;700&display=swap">
<style>
:root{
  --blue:#0255a3;
  --blue-deep:#02307a;
  --navy:#0a1a4a;
  --green:#acd036;
  --ink:#1b1b1b;
  --grey:#eaeaea;
  --white:#ffffff;
}
*{margin:0;padding:0;box-sizing:border-box}
html,body{width:1200px;height:3303px;overflow:hidden}
body{font-family:"Open Sans",Arial,sans-serif;color:var(--ink);background:var(--white);position:relative}
.section{position:absolute;left:0;width:1200px}
h2{font-family:"Arvo",Georgia,serif;font-weight:400;color:var(--blue);text-align:center;font-size:34px}

/* hero */
.hero{top:0;height:616px;overflow:hidden}
.hero-photo{position:absolute;inset:0;background:radial-gradient(ellipse at 65% 40%,#1d4fd6 0%,#1235b0 35%,#0b1f78 70%,#071446 100%)}
.site-header{position:absolute;top:0;left:0;width:1200px;height:80px}
.brand{position:absolute;left:132px;top:20px;font-family:"Open Sans",Arial,sans-serif;font-weight:700;font-size:32px;color:var(--green);letter-spacing:0.5px}
.main-nav{position:absolute;left:390px;top:30px;display:flex}
.main-nav a{color:var(--white);text-decoration:none;font-size:14px;margin-right:28px}
.main-nav a.active{color:var(--green)}
.btn-demo{position:absolute;left:927px;top:24px;width:141px;height:31px;background:var(--green);color:var(--navy);font-weight:700;font-size:12.5px;display:flex;align-items:center;justify-content:center;letter-spacing:0.3px}
.hero-title{position:absolute;left:132px;top:232px;font-family:"Arvo",Georgia,serif;font-size:41px;line-height:50px;color:var(--white);font-weight:400}
.btn-more{position:absolute;left:132px;top:341px;width:110px;height:33px;background:var(--green);color:var(--navy);font-family:"Arvo",Georgia,serif;font-size:12px;display:flex;align-items:center;justify-content:center}
.slide-arrow{position:absolute;width:30px;height:40px}
.hero .prev{left:40px;top:288px}
.hero .next{left:1130px;top:288px}

/* welcome */
.welcome{top:616px;height:266px}
.welcome h2{margin-top:72px}
.welcome p{width:936px;margin:14px auto 0;text-align:center;font-size:12.5px;line-height:24px;color:#333}

/* services */
.services{top:882px;height:450px;background:var(--grey)}
.services h2{margin-top:70px}
.service-card{position:absolute;top:138px;height:233px;background:var(--blue);text-align:center;color:var(--white)}
.service-card svg{margin-top:33px}
.service-card h3{font-family:"Arvo",Georgia,serif;font-weight:400;color:var(--green);font-size:21px;margin-top:10px}
.service-card p{font-size:10.5px;line-height:19px;width:250px;margin:8px auto 0;color:#dfe7f5}

/* industry */
.industry{top:1332px;height:436px}
.industry h2{position:absolute;left:132px;top:72px;text-align:left}
.industry-copy{position:absolute;left:132px;top:130px;width:440px;font-size:12px;line-height:21px;color:#333}
.industry-copy p{margin-bottom:20px}
.photo-shadow{position:absolute;left:645px;top:97px;width:423px;height:262px;background:#d9d9d9}
.industry-photo{position:absolute;left:630px;top:79px;width:422px;height:263px;background:linear-gradient(180deg,#1c2a5a 0%,#2c3d6e 45%,#6a5a4a 75%,#c0803a 100%)}

/* technology */
.technology{top:1768px;height:900px;background:linear-gradient(180deg,#acd036 0%,#b2d43f 40%,#a6cb30 100%);overflow:hidden}
.tech-texture{position:absolute;left:0;top:380px;width:1200px;height:520px;background:linear-gradient(180deg,rgba(172,208,54,0) 0%,rgba(150,185,40,0.35) 60%,rgba(140,175,35,0.45) 100%)}
.technology h2{margin-top:72px;position:relative}
.technology p{position:relative;width:936px;margin:12px auto 0;text-align:center;font-size:12px;line-height:19px;color:var(--ink)}
.tech-map{position:absolute;left:0;top:0}
.tech-label{position:absolute;font-size:19px;line-height:23px;color:var(--navy)}

/* testimonials */
.testimonials{top:2668px;height:520px}
.testimonials h2{margin-top:70px}
.quote-box{position:absolute;left:132px;top:135px;width:936px;height:251px;background:var(--grey);text-align:center}
.quote-box blockquote{font-size:17px;line-height:28px;color:#333;width:860px;margin:36px auto 0}
.quote-box cite{display:block;font-style:normal;color:var(--blue);font-size:17px;margin-top:17px}
.client-photo{position:absolute;left:539px;top:320px;width:122px;height:121px;background:linear-gradient(180deg,#8a8a8a,#4d4d4d);border:2px solid #fff}
.testimonials .prev{left:44px;top:250px}
.testimonials .next{left:1126px;top:250px}

/* footer */
.site-footer{top:3188px;height:115px;background:var(--blue);color:var(--white)}
.footer-nav{position:absolute;left:132px;top:33px;font-size:11px}
.footer-nav a{color:var(--white);text-decoration:none}
.footer-nav span{margin:0 8px}
.copyright{position:absolute;left:132px;top:66px;font-size:11px}
.social{position:absolute;top:50px;width:16px;height:16px;border-radius:50%;background:var(--white)}
</style>
</head>
<body>

<section class="section hero">
  <div class="hero-photo" role="img" aria-label="Blue-toned photo of an oil field worker in a hard hat holding a tablet in front of drilling rigs"></div>
  <header class="site-header">
    <div class="brand">OVRELDA</div>
    <nav class="main-nav">
      <a class="active" href="#">Home</a>
      <a href="#">Services</a>
      <a href="#">Industry Solutions</a>
      <a href="#">Technology</a>
      <a href="#">About</a>
      <a href="#">Contact</a>
    </nav>
    <a class="btn-demo">SCHEDULE A DEMO</a>
  </header>
  <h1 class="hero-title">Maecenas vel tortor<br>accumsan quam</h1>
  <a class="btn-more">LEARN MORE</a>
  <svg class="slide-arrow prev" viewBox="0 0 30 40"><path d="M20 6 L8 20 L20 34" fill="none" stroke="#b9c6ee" stroke-width="3"/></svg>
  <svg class="slide-arrow next" viewBox="0 0 30 40"><path d="M10 6 L22 20 L10 34" fill="none" stroke="#b9c6ee" stroke-width="3"/></svg>
</section>

<section class="section welcome">
  <h2>Welcome to Ovrelda</h2>
  <p>Nulla tristique posuere molestie. Aliquam erat volutpat. Etiam quis aliquet risus. Duis ornare erat eget magna dapibus, in accumsan quam pharetra. Nam tempus, quam in bibendum vulputate, sapien dolor viverra nisl, vitae euismod elit turpis et nulla. Aliquam erat volutpat. Pellentesque blandit lacus eget nunc faucibus, et tincidunt eros viverra. Phasellus consequat sagittis nisi suscipit feugiat. Cras eget leo sed nunc hendrerit ultricies eu at nisl.</p>
</section>

<section class="section services">
  <h2>Services</h2>
  <div class="service-card" style="left:132px;width:293px">
    <svg width="80" height="70" viewBox="0 0 80 70" fill="none" stroke="#fff" stroke-width="2"><rect x="5" y="6" width="70" height="44" rx="2"/><line x1="5" y1="42" x2="75" y2="42"/><path d="M40 16 L54 26 L40 36 L26 26 Z"/><path d="M32 26 L40 20 L48 26 L40 32 Z"/><line x1="30" y1="50" x2="26" y2="62"/><line x1="50" y1="50" x2="54" y2="62"/><line x1="22" y1="62" x2="58" y2="62"/></svg>
    <h3>Maecenas</h3>
    <p>Etiam mattis augue vehicula odio posuere, sit amet tempus lectus luctus. Nulla facilisi. Etiam vel massa elementum, bibendum tellus venenatis.</p>
  </div>
  <div class="service-card" style="left:454px;width:292px">
    <svg width="80" height="70" viewBox="0 0 80 70" fill="none" stroke="#fff" stroke-width="2"><circle cx="34" cy="40" r="20"/><path d="M34 40 L34 20 M34 40 L52 48"/><rect x="50" y="14" width="6" height="22"/><rect x="60" y="8" width="6" height="28"/><rect x="70" y="18" width="6" height="18"/><path d="M6 8 L20 8 L20 20"/><text x="8" y="18" fill="#fff" stroke="none" font-size="9">%</text></svg>
    <h3>Curabitur</h3>
    <p>Etiam mattis augue vehicula odio posuere, sit amet tempus lectus luctus. Nulla facilisi. Etiam vel massa elementum, bibendum tellus venenatis.</p>
  </div>
  <div class="service-card" style="left:773px;width:295px">
    <svg width="80" height="70" viewBox="0 0 80 70" fill="none" stroke="#fff" stroke-width="2"><rect x="10" y="6" width="60" height="50" rx="3"/><line x1="18" y1="18" x2="40" y2="18"/><line x1="18" y1="28" x2="36" y2="28"/><line x1="18" y1="38" x2="34" y2="38"/><circle cx="54" cy="34" r="10"/><path d="M48 44 L46 56 M60 44 L62 56"/><line x1="30" y1="56" x2="50" y2="64"/></svg>
    <h3>Quisque</h3>
    <p>Etiam mattis augue vehicula odio posuere, sit amet tempus lectus luctus. Nulla facilisi. Etiam vel massa elementum, bibendum tellus venenatis.</p>
  </div>
</section>

<section class="section industry">
  <h2>Industry Solutions</h2>
  <div class="industry-copy">
    <p>We offer solutions for wide variety of industries such as oil &amp; gas, industrial, health safety and environment (HSE) with an in-depth knowledge and experience of and back office flow information for oil &amp; gas industry which significantly reduces the cost of operations.</p>
    <p>We have in-depth knowledge and experience when it comes to servicing equipment's, tracking personnel and inventory for industrial machines. The solutions cater to predictive behavior rather than being reactive.</p>
    <p>We have in-depth knowledge and experience on avoiding safety incidents and managing site inspection lifecycles.</p>
  </div>
  <div class="photo-shadow"></div>
  <div class="industry-photo" role="img" aria-label="Photo of a field engineer in a hard hat and safety vest reviewing documents in front of a lit refinery at dusk"></div>
</section>

<section class="section technology">
  <div class="tech-texture" role="img" aria-label="Faint green-tinted photo of refinery towers"></div>
  <h2>Technology</h2>
  <p>We offer disruptive technology to connect field services, data collection using IoT, monitor assets in the field, automated feed from analysis results, automated workflows, integrate with enterprise systems, RFID, GPS asset tracking and process high volume data for analysis using big data technology. We mobilize field workers using mobile platforms, cloud technology for servicing, monitoring and prescribing.</p>
  <svg class="tech-map" width="1200" height="900" viewBox="0 0 1200 900">
    <g stroke="#fff" stroke-width="3">
      <line x1="599" y1="526" x2="599" y2="302"/><line x1="599" y1="526" x2="449" y2="385"/><line x1="599" y1="526" x2="766" y2="385"/>
      <line x1="599" y1="526" x2="376" y2="526"/><line x1="599" y1="526" x2="821" y2="526"/><line x1="599" y1="526" x2="449" y2="680"/>
      <line x1="599" y1="526" x2="766" y2="680"/><line x1="599" y1="526" x2="599" y2="751"/>
    </g>
    <g fill="#fff">
      <circle cx="599" cy="302" r="53"/><circle cx="449" cy="385" r="53"/><circle cx="766" cy="385" r="53"/>
      <circle cx="376" cy="526" r="53"/><circle cx="821" cy="526" r="53"/><circle cx="449" cy="680" r="53"/>
      <circle cx="766" cy="680" r="53"/><circle cx="599" cy="751" r="53"/><circle cx="599" cy="526" r="108"/>
    </g>
    <text x="599" y="541" text-anchor="middle" font-family="Open Sans, Arial, sans-serif" font-weight="600" font-size="38" fill="#0255a3">OVRELDA</text>
    <g fill="#0255a3">
      <path d="M586 312 h30 a9 9 0 0 0 0-18 a12 12 0 0 0-22-4 a9 9 0 0 0-8 22z"/>
      <circle cx="458" cy="375" r="6"/><circle cx="458" cy="395" r="6"/><circle cx="440" cy="385" r="6"/>
      <path d="M440 385 L458 375 M440 385 L458 395" stroke="#0255a3" stroke-width="3"/>
      <rect x="366" y="508" width="20" height="36" rx="3"/><rect x="370" y="514" width="12" height="22" fill="#fff"/>
      <path d="M819 540 a4 4 0 1 0 4 0z"/>
      <path d="M434 694 L446 680 L454 688 L466 672 M460 672 h6 v6" fill="none" stroke="#0255a3" stroke-width="4"/>
      <rect x="750" y="688" width="5" height="6"/><rect x="758" y="682" width="5" height="12"/><rect x="766" y="676" width="5" height="18"/><rect x="774" y="668" width="5" height="26"/>
      <rect x="584" y="750" width="5" height="14"/><rect x="592" y="740" width="5" height="24"/><rect x="600" y="746" width="5" height="18"/><rect x="608" y="736" width="5" height="28"/><rect x="580" y="766" width="38" height="3"/>
    </g>
    <g fill="none" stroke="#0255a3" stroke-width="4">
      <path d="M754 380 a13 13 0 0 1 23-6 M778 390 a13 13 0 0 1-23 6"/>
      <path d="M806 522 a20 20 0 0 1 30 0 M811 528 a13 13 0 0 1 20 0"/>
    </g>
    <path d="M774 370 l6 4 l-6 4z M758 400 l-6-4 l6-4z" fill="#0255a3"/>
  </svg>
  <div class="tech-label" style="left:499px;top:218px;width:200px;text-align:center">Cloud Platform</div>
  <div class="tech-label" style="left:187px;top:373px;width:200px;text-align:right">API &amp; Integration</div>
  <div class="tech-label" style="left:832px;top:350px">Automated &amp;<br>Configurable Workflows</div>
  <div class="tech-label" style="left:113px;top:514px;width:200px;text-align:right">Mobile Platform</div>
  <div class="tech-label" style="left:889px;top:492px">RFID &amp; GPS<br>Technology</div>
  <div class="tech-label" style="left:185px;top:668px;width:200px;text-align:right">Big Data</div>
  <div class="tech-label" style="left:832px;top:668px">IoT Ready</div>
  <div class="tech-label" style="left:474px;top:812px;width:250px;text-align:center">Analytics / ML / AI</div>
</section>

<section class="section testimonials">
  <h2>Testimonials</h2>
  <div class="quote-box">
    <blockquote>“ Fusce vitae lectus sit amet mi pulvinar maximus. Aenean placerat, nibh vel accumsan aliquet, magna nibh accumsan nibh, ac tempus nunc ipsum ac tellus. Cras augue magna, placerat eget nulla non, congue suscipit neque. Phasellus nisl est, condimentum vitae faucibus in, sollicitudin vel metus. ”</blockquote>
    <cite>Dana Rourke, Company name</cite>
  </div>
  <div class="client-photo" role="img" aria-label="Portrait photo of the client quoted"></div>
  <svg class="slide-arrow prev" viewBox="0 0 30 40"><path d="M20 8 L10 20 L20 32" fill="none" stroke="#999" stroke-width="2.5"/></svg>
  <svg class="slide-arrow next" viewBox="0 0 30 40"><path d="M10 8 L20 20 L10 32" fill="none" stroke="#999" stroke-width="2.5"/></svg>
</section>

<footer class="section site-footer">
  <nav class="footer-nav">
    <a href="#">Home</a><span>|</span><a href="#">Services</a><span>|</span><a href="#">Industry Solutions</a><span>|</span><a href="#">Technology</a><span>|</span><a href="#">About</a><span>|</span><a href="#">Contact</a>
  </nav>
  <div class="copyright">Copyright © 2018 Ovrelda. All rights reserved.</div>
  <span class="social" style="left:1006px" aria-label="Social link"></span>
  <span class="social" style="left:1050px" aria-label="Social link"></span>
</footer>

</body>
</html>
```